Ridgely Forge business card for handing simple contact information and generating service awareness

Utilizing the attached logo(s), generate a professional, but approachable, card conveying a sense of capability and integrity. Please only use one logo of the four attached; the different colors are all acceptable, but preference will be given to a design integrating a teal/turquoise logo,

I do not know where to put in the contact information or details?

Target Market(s)

Agriculture, Farming, Timber, Forestry, Construction, Crane Service

Industry/Entity Type

Contact Information for Business Card

Name, Phone Number, email address

Colors

Designer to choose colors to be used in the design.

Requirements
Nice to have
• It would be great to have either a mountain or one of the attached cranes as a backdrop on the rear of the card. Simple watermarks and/or Debossing is also great

```html
<!DOCTYPE html>
<html lang="en">
<head>
<meta charset="utf-8">
<title>Ridgely Forge – Business Card</title>
<link href="https://fonts.googleapis.com/css2?family=Poppins:wght@400;700&display=swap" rel="stylesheet">
<style>
  :root {
    --teal: #2a6e60;
    --teal-dark: #153b33;
    --teal-mid: #236154;
    --paper: #ffffff;
    --paper-shade: #e9eaea;
    --ink: #1d1d1d;
    --backdrop: #b9b9b9;
  }
  * { box-sizing: border-box; margin: 0; padding: 0; }
  html, body { width: 1200px; height: 900px; overflow: hidden; }
  body {
    background: var(--backdrop);
    font-family: "Poppins", sans-serif;
    position: relative;
  }
  .card {
    position: absolute;
    width: 560px;
    height: 320px;
    border-radius: 26px;
    overflow: hidden;
    box-shadow: 0 10px 24px rgba(0,0,0,.25);
  }
  .card--front {
    left: 120px; top: 100px;
    background: linear-gradient(160deg, var(--teal-dark) 0%, var(--teal) 45%, var(--teal-mid) 100%);
  }
  .card--back {
    left: 520px; top: 480px;
    background: linear-gradient(150deg, var(--paper) 40%, var(--paper-shade) 100%);
  }
  .watermark {
    position: absolute;
    right: -40px; top: -30px;
    width: 320px; height: 300px;
    border-radius: 50%;
  }
  .card--front .watermark {
    background: radial-gradient(circle at 50% 45%, rgba(255,255,255,.09), rgba(255,255,255,0) 70%);
  }
  .card--back .watermark {
    background: radial-gradient(circle at 50% 45%, rgba(0,0,0,.06), rgba(0,0,0,0) 70%);
  }
  .brand {
    display: flex;
    align-items: center;
    gap: 12px;
    font-weight: 700;
    text-transform: uppercase;
    letter-spacing: .04em;
  }
  .brand__dot {
    width: 22px; height: 22px;
    border-radius: 50%;
  }
  .card--front .brand {
    position: absolute;
    left: 50%; top: 50%;
    transform: translate(-50%, -50%);
    color: var(--paper);
    font-size: 34px;
    white-space: nowrap;
  }
  .card--front .brand__dot { background: var(--paper); }
  .card--back .brand {
    position: absolute;
    left: 40px; top: 46px;
    color: var(--teal);
    font-size: 28px;
  }
  .card--back .brand__dot { background: var(--teal); }
  .contact {
    position: absolute;
    left: 40px; bottom: 34px;
    color: var(--ink);
  }
  .contact__name {
    color: var(--teal);
    font-weight: 700;
    font-size: 24px;
    line-height: 1.1;
    text-transform: uppercase;
  }
  .contact__role {
    font-size: 17px;
    margin-bottom: 14px;
  }
  .contact__line {
    display: flex;
    align-items: center;
    gap: 8px;
    font-size: 17px;
    line-height: 1.45;
  }
  .contact__icon { width: 16px; height: 16px; fill: none; stroke: var(--teal); stroke-width: 2; }
</style>
</head>
<body>
  <section class="card card--front">
    <div class="watermark" role="img" aria-label="Faint mountain and tractor backdrop"></div>
    <div class="brand"><span class="brand__dot"></span>Ridgely Forge</div>
  </section>

  <section class="card card--back">
    <div class="watermark" role="img" aria-label="Faint mountain and tractor watermark"></div>
    <div class="brand"><span class="brand__dot"></span>Ridgely Forge</div>
    <div class="contact">
      <p class="contact__name">Callum Hartley</p>
      <p class="contact__role">Managing Director</p>
      <p class="contact__line">
        <svg class="contact__icon" viewBox="0 0 24 24"><path d="M5 3h4l2 5-2.5 1.5a11 11 0 0 0 6 6L16 13l5 2v4a2 2 0 0 1-2 2A16 16 0 0 1 3 5a2 2 0 0 1 2-2z"/></svg>
        055-214 738 190
      </p>
      <p class="contact__line">
        <svg class="contact__icon" viewBox="0 0 24 24"><rect x="3" y="5" width="18" height="14" rx="1"/><path d="M3 6l9 7 9-7"/></svg>
        hello@ridgelyforge.com
      </p>
    </div>
  </section>
</body>
</html>
```